I need business cards for my job as a performer. I want them to have the following information
Name: Dale Fenwick
Email Address: DaleRF7@corvelmail.example
Phone number: 0471963825
They should also say that I perform magic and Fire Spinning.

The information does not need to be in the format above, the performance types and especially the magic should be emphasized. I would like the design to be memorable but not gimmicky or tacky (a lot of magicians use things like playing cards with their details on them and I do NOT like this approach.) I just want an abstract, stylish design that people will remember.

I intend to judge the contest by looking at all the applicants, walking away for half an hour then picking between the ones I remember so if your design is not memorable, it will not win. Good Luck.

```html
<!DOCTYPE html>
<html lang="en">
<head>
<meta charset="utf-8">
<title>Dale Fenwick — Magic and Fire Spinning Business Card</title>
<link href="https://fonts.googleapis.com/css2?family=Cinzel:wght@400;500;600&family=UnifrakturMaguntia&display=swap" rel="stylesheet">
<style>
  :root {
    --sheet: #ffffff;
    --sheet-line: #8a8a8a;
    --ray-light: #1d1dcc;
    --ray-mid: #1414a8;
    --ray-dark: #0c0c7e;
    --back-glow: #1a26d2;
    --back-deep: #05055a;
    --gold-light: #f4e3a4;
    --gold: #d9b862;
    --gold-deep: #a27d2c;
    --shadow: #3d3d3d;
  }
  * { margin: 0; padding: 0; box-sizing: border-box; }
  html, body { width: 999px; height: 1200px; overflow: hidden; background: var(--sheet); }
  .sheet {
    position: relative; width: 999px; height: 1200px;
    border: 2px solid var(--sheet-line);
    background: var(--sheet);
  }
  .card {
    position: absolute; width: 715px; height: 403px; overflow: hidden;
    box-shadow: 9px 9px 0 var(--shadow);
  }
  .card--front { left: 131px; top: 161px; }
  .card--back {
    left: 133px; top: 620px;
    background: radial-gradient(ellipse 70% 75% at 45% 45%, var(--back-glow) 0%, #0e12a0 45%, var(--back-deep) 100%);
  }
  .sunburst {
    position: absolute; inset: 0;
    background: radial-gradient(ellipse 80% 90% at 46% 43%, var(--ray-light) 0%, var(--ray-mid) 55%, var(--ray-dark) 100%);
  }
  .gold-text {
    color: var(--gold);
    background: linear-gradient(180deg, var(--gold-light) 0%, var(--gold) 50%, var(--gold-deep) 100%);
    -webkit-background-clip: text; background-clip: text;
    -webkit-text-fill-color: transparent;
  }
  .gold-block {
    position: absolute;
    background: radial-gradient(ellipse at 50% 40%, var(--gold-light) 0%, var(--gold) 55%, rgba(162,125,44,0.6) 100%);
    border-radius: 6px;
  }
  .star-row { left: 138px; top: 130px; width: 240px; height: 46px; }
  .star-accent { left: 322px; top: 188px; width: 58px; height: 56px; }
  .fire-word { left: 294px; top: 310px; width: 125px; height: 34px; border-radius: 3px; }
  .performer-name {
    position: absolute; left: 97px; top: 22px;
    font-family: "UnifrakturMaguntia", "Times New Roman", serif;
    font-size: 82px; font-weight: 400; line-height: 1;
    white-space: nowrap;
  }
  .act {
    position: absolute; font-family: "Cinzel", serif; font-weight: 500;
    white-space: nowrap; line-height: 1;
  }
  .act--magic { left: 106px; top: 206px; font-size: 46px; }
  .act--and { left: 254px; top: 268px; font-size: 17px; }
  .act--spinning { left: 436px; top: 306px; font-size: 38px; }
  .back-name {
    position: absolute; left: 0; right: 0; top: 160px; text-align: center;
    font-family: "Cinzel", serif; font-size: 46px; font-weight: 400; letter-spacing: 2px;
    color: var(--gold);
  }
  .contact {
    position: absolute; left: 133px; top: 258px;
    font-family: "Cinzel", serif; font-size: 25px; line-height: 40px;
    letter-spacing: 1.5px; color: var(--gold); list-style: none;
  }
</style>
</head>
<body>
<main class="sheet">
  <section class="card card--front">
    <div class="sunburst" role="img" aria-label="Blue sunburst of radiating rays"></div>
    <h1 class="performer-name gold-text">Dale Fenwick</h1>
    <div class="gold-block star-row" role="img" aria-label="Row of gold stars growing in size"></div>
    <div class="gold-block star-accent" role="img" aria-label="Large gold star"></div>
    <p class="act act--magic gold-text">Magic</p>
    <p class="act act--and gold-text">and</p>
    <div class="gold-block fire-word" role="img" aria-label="Flame-styled lettering of the word Fire"></div>
    <p class="act act--spinning gold-text">Spinning</p>
  </section>

  <section class="card card--back">
    <h2 class="back-name">Dale Fenwick</h2>
    <ul class="contact">
      <li>Email: DaleRF7@corvelmail.example</li>
      <li>Phone number: 0471963825</li>
    </ul>
  </section>
</main>
</body>
</html>
```